Photography blog homepage design

I need a new webpage design for my photography blog. My blog focuses on post-processing techniques, particularly in luminosity masking, HDR photography and other advanced photo editing skills. I want the new homepage to let visitors know instantly what the blog is about as this is currently not very obvious from the feedback I received. Apart from that, the homepage should also inform/showcase latest blog post and/or popular blog post and/or some of the training courses I offer (that's my idea, but I leave it to your expertise). There should also ideally have a CTA that leads visitors to the "Start Here" page where they can learn more about my blog. The bulk of my audience is intermediate/advanced photographers who are above 30-35 years old, with a significant group in the 60 to >75 age group. The design should convey trust and creativity at the same time. The color theme for my blog is orange and dark grey. URL is www.lumivarnic.com, you can use the current content on that page.

Target Market(s)

Intermediate/advanced photographers (hobbyist or professional) age 35-75 years old.

Number of Pages Required

1 page

Font styles to use
Sans Serif

Colors
faa54b
f68e4e
f78f20

Requirements
Must have
• Upside down homepage (menus at the bottom)

```html
<!DOCTYPE html>
<html lang="en">
<head>
<meta charset="utf-8">
<title>Lumivarnic – Photo Editing Blog</title>
<link href="https://fonts.googleapis.com/css2?family=Poppins:wght@400;500;600;700&family=Montserrat:wght@400;500;600&family=Dosis:wght@400;500&display=swap" rel="stylesheet">
<style>
:root{
  --orange:#f78f20;
  --orange-soft:#faa54b;
  --orange-mid:#f68e4e;
  --dark:#2b2b2b;
  --ink:#222222;
  --grey:#555555;
  --teal:#3a887c;
  --brick:#a24a4a;
  --white:#ffffff;
  --black:#0b0b0b;
}
*{margin:0;padding:0;box-sizing:border-box}
html,body{width:1200px;height:2819px;overflow:hidden;background:var(--white)}
body{position:relative;font-family:'Poppins',sans-serif;color:var(--ink)}
.abs{position:absolute}

/* hero */
.top-bar{left:0;top:0;width:1200px;height:6px;background:var(--orange-soft)}
.hero{left:0;top:6px;width:1200px;height:471px;
  background:radial-gradient(ellipse at 45% 60%,#4a4a48 0%,#2c2c2c 45%,#1b1b1b 100%)}
.hero-shade{left:0;top:6px;width:1200px;height:471px;
  background:linear-gradient(90deg,rgba(20,20,20,.55),rgba(80,80,76,.15) 60%,rgba(120,118,110,.3))}
.brand{font-family:'Poppins',sans-serif;font-weight:700;color:var(--white);letter-spacing:.5px;display:flex;align-items:center;gap:8px}
.brand .dot{width:22px;height:22px;border-radius:50%;background:var(--orange)}
.hero-logo{left:85px;top:58px;font-size:30px}
.hero-title{left:0;top:208px;width:1200px;text-align:center;color:var(--white);font-size:28px;font-weight:400}
.hero-title b{font-weight:600}
.hero-sub{left:0;top:245px;width:1200px;text-align:center;color:var(--white);font-size:13.5px;font-family:'Montserrat',sans-serif}
.btn-ghost{height:44px;border:2px solid;border-radius:3px;display:flex;align-items:center;justify-content:center;font-size:11px;font-weight:600;font-family:'Montserrat',sans-serif}
.btn-start{left:428px;top:295px;width:156px;border-color:var(--orange);color:var(--orange)}
.btn-ebook{left:617px;top:295px;width:155px;border-color:var(--white);color:var(--white)}

/* section headings */
.section-title{font-size:22px;font-weight:600;letter-spacing:.3px;color:var(--ink)}
.rule{height:4px;width:60px;background:var(--orange)}

/* help band */
.help-band{left:0;top:686px;width:1200px;height:564px;
  background:linear-gradient(180deg,#3a4452 0%,#59616b 40%,#8b8f94 100%)}
.card{width:300px;height:400px;background:var(--white);box-shadow:0 2px 6px rgba(0,0,0,.25);border-radius:2px;overflow:hidden}
.card-photo{width:300px;height:234px}
.card h3{position:absolute;left:35px;top:254px;font-size:20px;font-weight:500;color:var(--ink)}
.card p{position:absolute;left:36px;top:302px;width:220px;font-size:10.5px;line-height:13px;font-weight:500;color:var(--ink)}
.card .btn-card{position:absolute;left:36px;top:354px;width:103px;height:29px;background:var(--orange);border-radius:2px;color:var(--ink);font-size:10.5px;font-weight:500;display:flex;align-items:center;justify-content:center}
.card .free{position:absolute;left:212px;top:361px;font-size:12px;font-weight:700;color:#1e7a1e}

/* blog */
.post-photo{width:146px;height:146px;background:linear-gradient(180deg,#7d6a6a,#3a3c44 60%,#6c7179)}
.post h4{position:absolute;left:163px;top:0;width:310px;font-size:14px;line-height:17px;font-weight:400;color:var(--ink)}
.post .meta{position:absolute;left:164px;top:38px;font-size:8.5px;color:var(--grey)}
.post .excerpt{position:absolute;left:164px;top:57px;width:350px;font-family:'Montserrat',sans-serif;font-size:9px;line-height:13px;color:#444}
.post .more{position:absolute;left:164px;top:139px;font-size:10px;color:var(--orange)}

.tutorial{width:471px;height:257px;overflow:hidden}
.tutorial .t-title{position:absolute;left:34px;top:16px;width:340px;font-family:'Dosis',sans-serif;font-size:29px;line-height:33px;color:rgba(255,255,255,.82)}
.tutorial .play{position:absolute;left:204px;top:96px}
.tutorial .art{position:absolute;right:0;bottom:0;width:200px;height:150px}
.teal{background:var(--teal)}
.brick{background:var(--brick)}

.btn-solid{background:var(--orange-soft);border:1px solid var(--orange);color:var(--ink);font-size:14px;border-radius:2px;display:flex;align-items:center;justify-content:center}

/* ebook */
.ebook-sub{left:85px;top:2308px;font-size:22px;color:var(--ink)}
.ebook-sub b{font-weight:600}
.benefits{left:85px;top:2392px;font-size:23px;line-height:35px;color:var(--ink);list-style:none}
.btn-get{left:85px;top:2559px;width:188px;height:58px;background:var(--orange-mid);border:1px solid var(--orange);border-radius:2px;color:var(--ink);font-size:22px;font-weight:600;display:flex;align-items:center;justify-content:center}
.book{left:898px;top:2283px;width:216px;height:368px;background:linear-gradient(180deg,#8d9aa6,#6f756f 50%,#566048);box-shadow:6px 4px 10px rgba(0,0,0,.35);border-right:8px solid #dcdcdc}

/* footer */
.footer{left:0;top:2769px;width:1200px;height:50px;background:var(--black)}
.foot-logo{left:83px;top:2776px;font-size:21px}
.foot-logo .dot{width:16px;height:16px}
.copyright{left:84px;top:2803px;font-size:7px;color:#cfcfcf}
.menu{right:86px;top:2785px;display:flex;gap:20px;list-style:none;font-size:10px;color:var(--white)}
.menu .active{color:var(--orange)}
</style>
</head>
<body>

<div class="abs top-bar"></div>
<div class="abs hero" role="img" aria-label="Photographer holding a camera with a large lens, outdoors"></div>
<div class="abs hero-shade"></div>
<div class="abs brand hero-logo"><span class="dot"></span>LUMIVARNIC</div>
<h1 class="abs hero-title">Be More <b>PRODUCTIVE</b> In Editing Without Spending More <b>TIME</b></h1>
<p class="abs hero-sub">Download the free 4-Step Editing Framework ebook. Use the KESTREL framework to boost your creativity and productivity.</p>
<a class="abs btn-ghost btn-start">START HERE</a>
<a class="abs btn-ghost btn-ebook">GET YOUR FREE EBOOK</a>

<h2 class="abs section-title" style="left:86px;top:596px">I NEED HELP WITH...</h2>
<div class="abs rule" style="left:86px;top:630px"></div>

<div class="abs help-band" role="img" aria-label="Laptop keyboard and camera on a desk, blurred"></div>

<div class="abs card" style="left:85px;top:769px">
  <div class="card-photo" role="img" aria-label="Dark tunnel lit by a row of ceiling lights" style="background:linear-gradient(180deg,#050505,#1a1a1a 60%,#3c4a55)"></div>
  <h3>Luminosity Masks</h3>
  <p>Want to learn luminosity masking but find it too hard? Signup to the free luminosity masks crash course.</p>
  <a class="btn-card">START NOW</a><span class="free">FREE</span>
</div>
<div class="abs card" style="left:450px;top:769px">
  <div class="card-photo" role="img" aria-label="Photographer checking a histogram on a camera screen" style="background:linear-gradient(180deg,#c9cdd0,#8b918f 55%,#4a4d4a)"></div>
  <h3>Histograms</h3>
  <p>Struggling to get the right exposure? Master histograms with this ebook to help you nail the exposure in every shot.</p>
  <a class="btn-card">START NOW</a><span class="free">FREE</span>
</div>
<div class="abs card" style="left:814px;top:769px">
  <div class="card-photo" role="img" aria-label="Person walking past a glowing blue wall at night" style="background:linear-gradient(180deg,#10108a,#2222ee 50%,#060640)"></div>
  <h3>Exposure Blending</h3>
  <p>Stop producing mediocre HDR. Get the Tonal Range Blueprint to start creating natural looking HDR images.</p>
  <a class="btn-card">START NOW</a><span class="free">FREE</span>
</div>

<h2 class="abs section-title" style="left:86px;top:1410px">FROM THE BLOG</h2>
<div class="abs rule" style="left:86px;top:1445px"></div>
<h2 class="abs section-title" style="left:643px;top:1410px">POPULAR TUTORIALS</h2>
<div class="abs rule" style="left:643px;top:1445px"></div>

<article class="abs post" style="left:85px;top:1483px;width:520px;height:160px">
  <div class="post-photo" role="img" aria-label="City street between tall buildings at dusk"></div>
  <h4>Creative Edit #18 – Create Halden Effect and Directing Focus Using Lightdesk</h4>
  <span class="meta">By Marlen Oswy / Blog</span>
  <p class="excerpt">Have you ever seen photographs (typically landscape images) where the subjects in the photo have a soft and glowing look to it? The effect is deliberate rather than a technical error by the photographer. As the matter of fact, it's called the Halden effect, named after the photographer who pioneered it. If you like to read ...</p>
  <a class="more">Read More »</a>
</article>
<article class="abs post" style="left:85px;top:1677px;width:520px;height:160px">
  <div class="post-photo" role="img" aria-label="City street between tall buildings at dusk"></div>
  <h4>Creative Edit #18 – Create Halden Effect and Directing Focus Using Lightdesk</h4>
  <span class="meta">By Marlen Oswy / Blog</span>
  <p class="excerpt">Have you ever seen photographs (typically landscape images) where the subjects in the photo have a soft and glowing look to it? The effect is deliberate rather than a technical error by the photographer. As the matter of fact, it's called the Halden effect, named after the photographer who pioneered it. If you like to read ...</p>
  <a class="more">Read More »</a>
</article>
<article class="abs post" style="left:85px;top:1869px;width:520px;height:160px">
  <div class="post-photo" role="img" aria-label="City street between tall buildings at dusk"></div>
  <h4>Creative Edit #18 – Create Halden Effect and Directing Focus Using Lightdesk</h4>
  <span class="meta">By Marlen Oswy / Blog</span>
  <p class="excerpt">Have you ever seen photographs (typically landscape images) where the subjects in the photo have a soft and glowing look to it? The effect is deliberate rather than a technical error by the photographer. As the matter of fact, it's called the Halden effect, named after the photographer who pioneered it. If you like to read ...</p>
  <a class="more">Read More »</a>
</article>

<div class="abs tutorial teal" style="left:643px;top:1482px">
  <p class="t-title">Saturation Mask: Fixing Color Saturation With Precision</p>
  <svg class="play" width="64" height="64" viewBox="0 0 64 64"><circle cx="32" cy="32" r="28" fill="none" stroke="#fff" stroke-width="5"/><path d="M25 19 L46 32 L25 45 Z" fill="#fff"/></svg>
  <div class="art" role="img" aria-label="Illustration of stacked adjustment panels with sliders" style="background:linear-gradient(135deg,rgba(0,0,0,0) 40%,rgba(0,0,0,.15) 40%)"></div>
</div>
<div class="abs tutorial brick" style="left:643px;top:1756px">
  <p class="t-title">Create Razor Sharp Images With Focus Stacking</p>
  <svg class="play" width="64" height="64" viewBox="0 0 64 64"><circle cx="32" cy="32" r="28" fill="none" stroke="#fff" stroke-width="5"/><path d="M25 19 L46 32 L25 45 Z" fill="#fff"/></svg>
  <div class="art" role="img" aria-label="Illustration of a focus target framed by hands" style="background:linear-gradient(135deg,rgba(0,0,0,0) 40%,rgba(0,0,0,.15) 40%)"></div>
</div>

<a class="abs btn-solid" style="left:270px;top:2048px;width:146px;height:42px">Browse Our Blog</a>
<a class="abs btn-solid" style="left:806px;top:2048px;width:145px;height:42px">Browse Tutorials</a>

<h2 class="abs section-title" style="left:86px;top:2240px">GET YOUR FREE EBOOK NOW</h2>
<div class="abs rule" style="left:86px;top:2276px"></div>
<p class="abs ebook-sub">How To Create Powerful Images Consistently <b>Without More Effort</b></p>
<ul class="abs benefits">
  <li>+ More productive in editing with less time</li>
  <li>+ Find endless inspiration for creativity</li>
  <li>+ Apply the framework to all kinds of images</li>
</ul>
<a class="abs btn-get">GET IT NOW</a>
<div class="abs book" role="img" aria-label="Ebook cover: The 4-Step Editing Framework, with a cliff-top monastery"></div>

<footer class="abs footer"></footer>
<div class="abs brand foot-logo"><span class="dot"></span>LUMIVARNIC</div>
<p class="abs copyright">Copyright © 2019 Lumivarnic - All Rights Reserved.</p>
<ul class="abs menu">
  <li class="active">Home</li><li>About me</li><li>Courses</li><li>Blog</li><li>Ebook</li><li>FAQ</li><li>Contact</li>
</ul>

</body>
</html>
```